7 page website for Dog Training Business

we are seeking a website design that should be 7 pages for a Las Vegas Dog training business. the site will have a heavy focus on video, and social media. Ideas design can be borrowed from http://bramblevox.net
attached is a copy of the logo and business card mock up. Content is currently being written and will be posted shortly

Training

```html
<!DOCTYPE html>
<html lang="en">
<head>
<meta charset="utf-8">
<title>Pawley Dog Training</title>
<link href="https://fonts.googleapis.com/css2?family=Oswald:wght@300;400;500&family=Arimo:ital,wght@0,400;0,700;1,400&display=swap" rel="stylesheet">
<style>
:root{
  --lime:#8fbb3c;
  --lime-dark:#7aa62e;
  --accent:#a9c23a;
  --brown:#5b3822;
  --brown-dark:#4a2d1a;
  --pink:#e8605d;
  --nav:#f2f1ec;
  --nav-line:#d9d7cc;
  --ink:#555;
  --white:#fff;
}
*{box-sizing:border-box;margin:0;padding:0}
html,body{width:742px;height:1200px;overflow:hidden}
body{background:var(--lime);font-family:"Arimo",Arial,sans-serif;color:var(--ink);position:relative}
.topline{position:absolute;left:0;top:0;width:742px;height:4px;background:var(--lime-dark)}
.brand{position:absolute;left:78px;top:22px;display:flex;align-items:center;gap:8px}
.brand-dot{width:70px;height:70px;border-radius:50%;background:var(--brown)}
.brand-name{font-family:"Oswald",sans-serif;font-weight:500;font-size:20px;color:var(--brown);line-height:1.05;letter-spacing:1px}
.header-bar{position:absolute;right:62px;top:66px;display:flex;align-items:center;gap:6px;font-family:"Oswald",sans-serif;font-size:11px;letter-spacing:1px;color:var(--white)}
.header-bar .txt{margin-right:8px;display:flex;align-items:center;gap:5px}
.social{width:22px;height:22px;border-radius:2px}
.s1{background:#3b5998}.s2{background:#d34836}.s3{background:#b31217}.s4{background:#517fa4}.s5{background:#e5006d}.s6{background:#1da1f2}
.page{position:absolute;left:70px;top:113px;width:610px}
.nav{display:flex;height:47px;background:var(--nav);border-bottom:1px solid var(--nav-line)}
.nav a{flex:auto;display:flex;flex-direction:column;align-items:center;justify-content:center;gap:5px;text-decoration:none;color:var(--brown);font-family:"Oswald",sans-serif;font-size:10px;letter-spacing:1px;border-right:1px solid var(--nav-line)}
.nav a:last-child{border-right:0}
.nav i{width:8px;height:8px;border-radius:50%;background:var(--accent);display:block}
.video{height:236px;background:var(--brown);position:relative}
.video h2{position:absolute;left:10px;top:20px;font-family:"Oswald",sans-serif;font-weight:300;font-size:22px;color:var(--white);letter-spacing:1px;display:flex;align-items:center;gap:8px}
.player{position:absolute;left:8px;top:60px;width:391px;height:164px;background:#111}
.player-title{position:absolute;left:6px;top:4px;color:#eee;font-size:9px}
.player-frame{position:absolute;left:0;top:18px;width:391px;height:124px;background:linear-gradient(180deg,#6e6a6c,#8a7a6a 60%,#6b5c4f)}
.player-play{position:absolute;left:180px;top:70px;width:30px;height:22px;background:rgba(20,20,20,.8);border-radius:4px}
.player-play:after{content:"";position:absolute;left:12px;top:6px;border-left:9px solid #fff;border-top:5px solid transparent;border-bottom:5px solid transparent}
.player-bar{position:absolute;left:0;bottom:0;width:391px;height:22px;background:#1b1b1b;color:#bbb;font-size:7px;padding:8px 0 0 44px}
.playlist{position:absolute;left:410px;top:2px;width:200px}
.item{display:flex;gap:6px;height:34px;margin-bottom:1px;padding:2px 0;align-items:center}
.item.active{background:var(--pink)}
.thumb{width:38px;height:30px;flex:none;background:linear-gradient(135deg,#6f7f90,#8d7a62)}
.item b{display:block;font-family:"Oswald",sans-serif;font-weight:400;font-size:9px;color:#d7e46a;letter-spacing:.5px}
.item.active b{color:var(--white)}
.item span{font-size:8px;color:var(--white)}
.quotes{height:139px;background:var(--white);display:flex;gap:26px;padding:22px 16px 0}
.quote{flex:1;font-style:italic;font-size:9.6px;line-height:1.4;color:var(--ink)}
.quote .mark{color:var(--accent);font-weight:700;font-style:normal;font-size:13px;line-height:0}
.quote .by{margin-top:10px;font-style:normal;color:var(--accent)}
.slider{height:154px;position:relative;background:linear-gradient(90deg,#7d9a52,#9aa868 45%,#6f8b3c)}
.caption{position:absolute;left:0;bottom:0;width:100%;height:20px;background:rgba(40,40,40,.7);color:var(--white);font-family:"Oswald",sans-serif;font-size:10px;letter-spacing:1.5px;text-align:right;padding:4px 8px}
.gallery-link{height:19px;background:var(--pink);color:var(--white);font-family:"Oswald",sans-serif;font-size:9px;letter-spacing:1.5px;text-align:center;padding-top:4px}
.texts{height:276px;background:var(--white);display:flex;padding:24px 16px 0}
.col{flex:1;padding:0 8px}
.col+.col{border-left:1px solid #eadfd2}
.col h3{font-family:"Oswald",sans-serif;font-weight:300;font-size:18px;color:var(--brown-dark);letter-spacing:1px;margin-bottom:12px;display:flex;align-items:center;gap:7px}
.col h3 i{width:11px;height:11px;border-radius:50%;background:var(--brown);display:block}
.col p{font-size:7.4px;line-height:1.7;text-align:justify;color:var(--ink)}
.pic{float:left;width:138px;height:68px;margin:0 8px 4px 0;border:3px solid #eee;background:linear-gradient(135deg,#7c9a45,#b08a5a)}
.footer{height:203px;background:var(--brown);position:relative}
.footer-brand{position:absolute;left:24px;top:18px;display:flex;align-items:center;gap:8px}
.footer-brand .brand-dot{width:96px;height:96px;background:var(--accent)}
.footer-brand .brand-name{color:var(--white)}
.footer-rule{position:absolute;left:24px;top:128px;width:100px;height:1px;background:#8c6a52}
.contact{position:absolute;left:24px;top:136px;list-style:none;font-size:7.4px;color:#f1e6da;line-height:1.55}
.contact li{display:flex;align-items:center;gap:7px}
.contact li:first-child{font-weight:700;color:var(--white)}
.contact i{width:6px;height:6px;background:var(--accent);border-radius:50%;display:block}
.map{position:absolute;left:313px;top:17px;width:240px;height:156px;background:linear-gradient(135deg,#e8e2cf,#d8cfb4 50%,#e6dfc9)}
</style>
</head>
<body>
<div class="topline"></div>

<div class="brand">
  <div class="brand-dot"></div>
  <div class="brand-name">PAWLEY<br>DOG TRAINING</div>
</div>

<div class="header-bar">
  <span class="txt">
    <svg width="10" height="10" viewBox="0 0 10 10"><path d="M2 0.5l2 2-1 1.2c.6 1.3 1.6 2.3 2.9 2.9L7 5.5l2 2-1.3 1.8C4 9 1 6 .7 1.8z" fill="#fff"/></svg>
    1-555-0199 CONTACT US • FOLLOW US!
  </span>
  <span class="social s1"></span><span class="social s2"></span><span class="social s3"></span>
  <span class="social s4"></span><span class="social s5"></span><span class="social s6"></span>
</div>

<main class="page">
  <nav class="nav">
    <a href="#"><i></i>HOME</a>
    <a href="#"><i></i>ABOUT</a>
    <a href="#"><i></i>SERVICES / RATES</a>
    <a href="#"><i></i>PHOTOS / VIDEOS</a>
    <a href="#"><i></i>FAQ</a>
    <a href="#"><i></i>TESTIMONIALS</a>
    <a href="#"><i></i>PDT TIPS</a>
    <a href="#"><i></i>STORE</a>
    <a href="#"><i></i>CONTACT</a>
  </nav>

  <section class="video">
    <h2><svg width="18" height="13" viewBox="0 0 18 13"><rect width="18" height="13" rx="3" fill="#e8605d"/><path d="M7 3.5l5 3-5 3z" fill="#fff"/></svg>WATCH OUR VIDEOS!</h2>
    <div class="player">
      <div class="player-title">Loose Leash Walk: Calm Down!</div>
      <div class="player-frame" role="img" aria-label="Video still of a trainer walking a dog on a leash"></div>
      <div class="player-play"></div>
      <div class="player-bar">0:00 / 3:44</div>
    </div>
    <div class="playlist">
      <div class="item"><div class="thumb" role="img" aria-label="Video thumbnail"></div><div><b>FIRST VIDEO LINK</b><span>This is a subtitle</span></div></div>
      <div class="item"><div class="thumb" role="img" aria-label="Video thumbnail"></div><div><b>ANOTHER VIDEO</b><span>unt ut labore et dolore m</span></div></div>
      <div class="item active"><div class="thumb" role="img" aria-label="Video thumbnail"></div><div><b>DO EIUSMOD TE</b><span>iusmod tempor incid</span></div></div>
      <div class="item"><div class="thumb" role="img" aria-label="Video thumbnail"></div><div><b>LOREM IPSUM DOLOR SIT AMET</b><span>m ad minim ip ex ea commodo</span></div></div>
      <div class="item"><div class="thumb" role="img" aria-label="Video thumbnail"></div><div><b>SCING ELIT, SED</b><span>do consequat. Duis aute irure do</span></div></div>
    </div>
  </section>

  <section class="quotes">
    <blockquote class="quote"><span class="mark">“</span> Lorem ipsum dolor sit amet, consectetur adipiscing elit, sed do eiusmod tempor incididunt ut labore et dolore magna aliqua. Ut enim ad minim ip ex ea commodo consequat. Duis aute irure dolo <span class="mark">”</span><div class="by">- by John Doe</div></blockquote>
    <blockquote class="quote"><span class="mark">“</span> Lorem ipsum dolor sit amet, consectetur adipiscing elimod tempor incididunt ut labore et dolore magna aliqua. Ut enim ad minim ip ex ea commodo consequat. Duis aute irure dolo <span class="mark">”</span><div class="by">- by John Doe</div></blockquote>
    <blockquote class="quote"><span class="mark">“</span> Lorem ipsum dolor sit amet, consectetur adipiscing por incididunt ut labore et dolore magna aliqua. Ut enim ad minim ip ex ea commodo consequat. Duis aute irure dolo <span class="mark">”</span><div class="by">- by John Doe</div></blockquote>
  </section>

  <section class="slider" role="img" aria-label="Photo of a trainer kneeling on grass while a shepherd dog runs past">
    <div class="caption">THIS IS A CAPTION ABOUT DOGS</div>
  </section>
  <div class="gallery-link">■ LINK TO A PHOTO GALLERY</div>

  <section class="texts">
    <article class="col">
      <h3><i></i>THIS IS A TEXT</h3>
      <div class="pic" role="img" aria-label="Photo of a trainer with a shepherd dog on grass"></div>
      <p>At vero eos et accusamus et iusto odio dignissimos ducimus qui blanditiis praesentium voluptatum deleniti atque corrupti quos dolores et quas molestias excepturi sint occaecati cupiditate non provident, similique sunt in culpa qui officia deserunt mollitia animi, id est laborum et dolorum fuga. Et harum quidem rerum facilis est et expedita distinctio. Nam libero tempore, cum soluta nobis est eligendi optio cumque nihil impedit quo minus id quod maxime placeat facere possimus, omnis voluptas assumenda est, omnis dolor repellendus. Temporibus autem quibusdam et aut officiis debitis aut rerum necessitatibus saepe eveniet ut et voluptates repudiandae sint et molestiae non recusandae. Itaque earum rerum hic tenetur a sapiente delectus, ut aut reiciendis voluptatibus maiores alias consequatur aut perferendis doloribus asperiores repellat.</p>
    </article>
    <article class="col">
      <h3><i></i>THIS IS ANOTHER TEXT</h3>
      <div class="pic" role="img" aria-label="Photo of a dog running with a ball on a lawn"></div>
      <p>At vero eos et accusamus et iusto odio dignissimos ducimus qui blanditiis praesentium voluptatum deleniti atque corrupti quos dolores et quas molestias excepturi sint occaecati cupiditate non provident, similique sunt in culpa qui officia deserunt mollitia animi, id est laborum et doloruest, omnis dolor repellendus. Temporibus autem quibusdam et aut officiis debitis aut rerum necessitatibus saepe eveniet ut et voluptates repudiandae sint et molestiae non recusandae. Itaque earum rerum hic tenetur a sapiente delectus, ut aut reiciendis voluptatibus maiores alias consequatur aut perferendis doloribus asperiores repellat.</p>
    </article>
  </section>

  <footer class="footer">
    <div class="footer-brand">
      <div class="brand-dot"></div>
      <div class="brand-name">PAWLEY<br>DOG TRAINING</div>
    </div>
    <div class="footer-rule"></div>
    <ul class="contact">
      <li><i></i>1820 Juniper Ridge Road, Las Vegas, NV, USA</li>
      <li><i></i>Telephone: +1 702-555-0142</li>
      <li><i></i>Fax: +1 702-555-0143</li>
      <li><i></i>Email: hello@pawleydogs.com</li>
    </ul>
    <div class="map" role="img" aria-label="Street map of Las Vegas, Nevada"></div>
  </footer>
</main>
</body>
</html>
```